Flyer for Consulting Services (PM+Dev-Lead)

• The attached document describes consulting services for StartUps or young companies with a digital buisness model. We provide services for product management and development lead/scrum master. The target group of the flyer (i.e. who reads that flyer) is CEOs of Startups, Founders, Investors, Business Angle.s
• The task is to design an A4 flyer with one page layout (one pager) mostly for electronic destribution (printing second choice). There have to be two versions according given input: one in German and one in English with same layout. Preferably a format which allows us to adjust wording (e.g. Word, MS Publisher, …)
The final design should deliver professionality on one side and agility/StartUp mentality on the other side.

```html
<!DOCTYPE html>
<html lang="en">
<head>
<meta charset="utf-8">
<title>Product Management &amp; Development Partner Flyer</title>
<link rel="stylesheet" href="https://fonts.googleapis.com/css2?family=Alegreya:wght@700&family=Source+Sans+3:wght@400;600;700&display=swap">
<style>
:root{
  --blue:#1a72bd;
  --navy:#2c5aa8;
  --head-blue:#2a5fa8;
  --purple-1:#8e2a8f;
  --purple-2:#a8449f;
  --purple-3:#b552a8;
  --purple-4:#c879b4;
  --panel:#f1f2f4;
  --text:#3a3a3a;
  --rule:#c9ccd2;
}
*{margin:0;padding:0;box-sizing:border-box}
html,body{width:862px;height:1200px;overflow:hidden;background:#fff}
body{position:relative;font-family:"Source Sans 3",sans-serif;color:var(--text)}
.abs{position:absolute}
.header{left:13px;top:14px;width:835px;height:107px;background:var(--blue);color:#fff}
.header .name{font-family:"Alegreya",serif;font-weight:700;font-size:22px;letter-spacing:.3px}
.header .role{font-size:17px;margin-top:2px}
.header .left{position:absolute;left:43px;top:34px}
.header .right{position:absolute;right:42px;top:34px;text-align:right}
.hero{left:13px;top:121px;width:835px;height:448px;background:linear-gradient(120deg,#2e4150 0%,#6b7a86 35%,#c9c3bb 60%,#8c8f95 100%)}
.strip{left:13px;top:569px;width:835px;height:14px;background:var(--blue)}
.questions{left:13px;top:583px;width:835px;height:90px;display:flex;color:#fff}
.questions div{display:flex;align-items:center;justify-content:center;text-align:center;font-weight:600;font-size:17px;line-height:1.35}
.q-you{width:205px;background:var(--purple-1);justify-content:flex-start!important;padding:36px 0 0 45px;font-size:32px!important;font-weight:700!important}
.q1{width:163px;background:var(--purple-2)}
.q2{width:178px;background:var(--purple-3)}
.q3{width:289px;background:var(--purple-4)}
.claim{left:13px;top:673px;width:835px;height:43px;background:var(--navy);color:#fff;font-weight:700;font-size:25px;line-height:43px;padding-left:43px}
.panel{left:13px;top:716px;width:835px;height:345px;background:var(--panel);box-shadow:0 6px 8px -4px rgba(0,0,0,.35)}
.vrule{left:430px;top:732px;width:1px;height:320px;background:var(--rule)}
.hrule{left:58px;top:914px;width:750px;height:1px;background:var(--rule)}
.block h3{color:var(--head-blue);font-weight:700;font-size:15px;letter-spacing:.3px;margin-bottom:8px}
.block ul{list-style:none}
.block li{position:relative;padding-left:18px;font-size:13px;line-height:16px;margin-bottom:6px}
.block li svg{position:absolute;left:0;top:3px;width:10px;height:10px}
.contact-title{left:0;top:1071px;width:862px;text-align:center;color:var(--head-blue);font-weight:700;font-size:20px}
.contact-divider{left:429px;top:1100px;width:2px;height:44px;background:#888;opacity:.5}
.person{font-size:13px}
.person .pname{color:var(--head-blue);font-weight:700;font-size:15px;margin-bottom:7px}
.person .line{display:flex;gap:16px;align-items:center}
.person span{display:inline-flex;align-items:center;gap:4px}
.person svg{width:11px;height:11px}
.footer{left:13px;top:1159px;width:835px;height:24px;background:var(--navy)}
</style>
</head>
<body>
<svg width="0" height="0" style="position:absolute">
  <symbol id="tick" viewBox="0 0 10 10"><circle cx="5" cy="5" r="5" fill="#2a5fa8"/><path d="M2.8 5.2l1.5 1.5 3-3.2" stroke="#fff" stroke-width="1.3" fill="none"/></symbol>
  <symbol id="phone" viewBox="0 0 12 12"><circle cx="6" cy="6" r="5.3" fill="none" stroke="#8e2a8f" stroke-width="1.3"/><path d="M3.5 5.5h5v2.5h-5z M4 5.5q2-2.5 4 0" fill="#8e2a8f"/></symbol>
  <symbol id="mail" viewBox="0 0 12 12"><circle cx="6" cy="6" r="5.3" fill="none" stroke="#8e2a8f" stroke-width="1.3"/><path d="M3.3 4.3h5.4v3.6H3.3z M3.3 4.3l2.7 2 2.7-2" fill="none" stroke="#8e2a8f" stroke-width="1"/></symbol>
</svg>

<header class="abs header">
  <div class="left"><div class="name">Mathis Brandauer</div><div class="role">Agile Product Manager</div></div>
  <div class="right"><div class="name">Lukas Feldhaus &amp; Novatri GmbH</div><div class="role">Scrum Master, Dev-Lead</div></div>
</header>

<div class="abs hero" role="img" aria-label="Photo of a smiling team meeting around a conference table with a tablet"></div>
<div class="abs strip"></div>

<section class="abs questions">
  <div class="q-you">You …</div>
  <div class="q1">Have a digital<br>business idea?</div>
  <div class="q2">Already obtained<br>a funding?</div>
  <div class="q3">Are looking for<br>experienced support for<br>product development?</div>
</section>

<div class="abs claim">We are your partner for product management and development!</div>

<div class="abs panel"></div>
<div class="abs vrule"></div>
<div class="abs hrule"></div>

<section class="abs block" style="left:57px;top:730px;width:350px">
  <h3>WE …</h3>
  <ul>
    <li><svg><use href="#tick"/></svg>Take over interim roles as:Product Owner, Scrum Master, and Dev-Lead</li>
    <li><svg><use href="#tick"/></svg>Create your development team, optionally with offshore/nearshore locations</li>
    <li><svg><use href="#tick"/></svg>Setup the cloud environment for your solution and support its operations</li>
    <li><svg><use href="#tick"/></svg>Jointly establish an agile/lean mindset including corresponding procedures</li>
  </ul>
</section>

<section class="abs block" style="left:462px;top:730px;width:300px">
  <h3>IF WANTED, …</h3>
  <ul>
    <li><svg><use href="#tick"/></svg>Together we evolve your strategic orientation</li>
    <li><svg><use href="#tick"/></svg>Support you in architectureand technology design</li>
    <li><svg><use href="#tick"/></svg>Train you in product management and in creating a scalable agile organisation</li>
  </ul>
</section>

<section class="abs block" style="left:59px;top:928px;width:320px">
  <h3>YOUR BENEFITS</h3>
  <ul>
    <li><svg><use href="#tick"/></svg>You focus on your ideas and your business model</li>
    <li><svg><use href="#tick"/></svg>You receive a professional realization of your ideas – in quality, time and budget</li>
    <li><svg><use href="#tick"/></svg>Our lean/agile mindset supports your start-upmentality and your commercial success</li>
  </ul>
</section>

<section class="abs block" style="left:462px;top:928px;width:330px">
  <h3>WHY US?</h3>
  <ul>
    <li><svg><use href="#tick"/></svg>Combined expertise in product management, development, and operations</li>
    <li><svg><use href="#tick"/></svg>Founders with experiences in digital business models and numerous industries</li>
  </ul>
</section>

<h2 class="abs contact-title">How to Contact Us?</h2>
<div class="abs contact-divider"></div>

<div class="abs person" style="left:56px;top:1111px">
  <div class="pname">Mathis Brandauer</div>
  <div class="line"><span><svg><use href="#phone"/></svg>+49-170-55 12 40 87</span><span><svg><use href="#mail"/></svg>hello@brandauer-consult.de</span></div>
</div>

<div class="abs person" style="left:495px;top:1107px">
  <div class="pname">Lukas Feldhaus</div>
  <div class="line"><span><svg><use href="#phone"/></svg>+49-171-3 60 92 15</span><span><svg><use href="#mail"/></svg>lukas.feldhaus@novatri.com</span></div>
</div>

<div class="abs footer"></div>
</body>
</html>
```